Local Flower Farm Needs Business Card Design

I need business cards designed for a flower farm based in Eudora, Kansas.
Business Info:
We are a local cut flower farm located in Eudora, Kansas, founded by Darla Hoffstrom. What started as a passion for agriculture and search for more joy in daily life has blossomed into a small business dedicated to providing the community with beautiful, fresh, and sustainable flowers. We specialize in local, seasonal blooms, ensuring that every petal reflects the care and dedication we pour into our craft. Our mission is to deliver the highest quality flowers directly to our customers through local farmers markets and to florists who share our commitment to sustainability. Join us in celebrating the beauty of nature, one bloom at a time!
Contact Details:
Darla Hoffstrom
Owner
Phone 913-555-0147
Facebook: Lorabelle Quinn Blossoms
Instagram: @LorabelleQuinnBlossoms
Website: LorabelleQuinnBlossoms.example
Target Market(s)
Wholesale to Florists and Direct to Consumer via Farmers Market
Industry/Entity Type
Florist, Farm
Contact Information for Business Card
Name, Contact Info, Logo
Look and feel

```html
<!DOCTYPE html>
<html lang="en">
<head>
<meta charset="utf-8">
<title>Lorabelle Quinn Blossoms – Business Card</title>
<link rel="stylesheet" href="https://fonts.googleapis.com/css2?family=Libre+Caslon+Text:wght@400;700&display=swap">
<style>
  :root {
    --teal: #0a2a30;
    --paper: #ffffff;
    --backdrop: #1f2122;
    --ink-light: #f3f5f4;
  }
  * { margin: 0; padding: 0; box-sizing: border-box; }
  html, body {
    width: 1200px; height: 1200px; overflow: hidden;
    background: var(--backdrop);
    font-family: "Libre Caslon Text", Georgia, serif;
  }
  .card {
    position: absolute; left: 160px; width: 880px; height: 503px;
    overflow: hidden;
  }
  /* Back side */
  .card-back { top: 62px; background: var(--teal); color: var(--ink-light); }
  .brand-seal {
    position: absolute; border-radius: 50%;
    display: flex; flex-direction: column; align-items: center; justify-content: center;
    text-align: center; text-transform: uppercase; letter-spacing: 3px;
    line-height: 1.35; font-weight: 400;
  }
  .card-back .brand-seal {
    left: 320px; top: 70px; width: 240px; height: 240px;
    border: 1.5px solid var(--ink-light); color: var(--ink-light); font-size: 19px;
  }
  .back-url {
    position: absolute; left: 0; right: 0; top: 390px; text-align: center;
    font-size: 18px; letter-spacing: 6px; text-transform: uppercase;
  }
  /* Front side */
  .card-front { top: 637px; background: var(--teal); color: var(--ink-light); }
  .front-band { position: absolute; left: 0; top: 0; width: 100%; height: 236px; background: var(--paper); }
  .holder { position: absolute; left: 52px; top: 44px; color: var(--teal); }
  .holder-name { font-size: 31px; letter-spacing: 2px; text-transform: uppercase; font-weight: 400; }
  .holder-role { font-size: 17px; font-weight: 700; margin-top: 2px; }
  .card-front .brand-seal {
    left: 342px; top: 186px; width: 236px; height: 236px;
    background: var(--paper); color: var(--teal); font-size: 19px;
  }
  .contact-list { position: absolute; left: 40px; top: 368px; list-style: none; font-size: 22px; }
  .contact-list li { display: flex; align-items: center; gap: 12px; height: 38px; }
  .contact-list svg { width: 24px; height: 24px; flex: none; }
  .social-list {
    position: absolute; right: 36px; top: 392px; list-style: none; font-size: 22px; text-align: right;
  }
  .social-list li { display: flex; align-items: center; justify-content: flex-end; gap: 12px; height: 36px; }
  .social-dot { width: 24px; height: 24px; border: 1.5px solid var(--ink-light); border-radius: 50%; flex: none; }
</style>
</head>
<body>
  <section class="card card-back" aria-label="Card back">
    <div class="brand-seal">Lorabelle<br>Quinn<br>Blossoms</div>
    <p class="back-url">www.lorabellequinnblossoms.example</p>
  </section>

  <section class="card card-front" aria-label="Card front">
    <div class="front-band"></div>
    <div class="holder">
      <h1 class="holder-name">Darla Hoffstrom</h1>
      <p class="holder-role">Owner</p>
    </div>
    <div class="brand-seal">Lorabelle<br>Quinn<br>Blossoms</div>
    <ul class="contact-list">
      <li>
        <svg viewBox="0 0 24 24" fill="none" stroke="#f3f5f4" stroke-width="1.5">
          <circle cx="12" cy="12" r="11"/>
          <path d="M9 6.5l2 3-1.3 1.2c.6 1.5 1.7 2.6 3.2 3.3l1.2-1.3 3 2-1.2 2c-4.5-.3-8.3-4-8.6-8.6z" fill="#f3f5f4" stroke="none"/>
        </svg>
        <span>913-555-0147</span>
      </li>
      <li>
        <svg viewBox="0 0 24 24" fill="none" stroke="#f3f5f4" stroke-width="1.3">
          <circle cx="12" cy="12" r="11"/>
          <circle cx="12" cy="12" r="7"/>
          <ellipse cx="12" cy="12" rx="3" ry="7"/>
          <path d="M5 12h14M6 8.5h12M6 15.5h12"/>
        </svg>
        <span>LorabelleQuinnBlossoms.example</span>
      </li>
    </ul>
    <ul class="social-list">
      <li><span>Lorabelle Quinn Blossoms</span><span class="social-dot"></span></li>
      <li><span>@LorabelleQuinnBlossoms</span><span class="social-dot"></span></li>
    </ul>
  </section>
</body>
</html>
```